Web design for boutique law firm

Web design for law firm; practice areas include:
-international intellectual property counseling
-general corporate (contract negotiation, licensing, distribution agreements
-see my *very* outdated website at www.pvtlegalhouse.com: here is some of the home page content:

"PVT Law Group enjoys providing proactive, business-minded, efficient legal solutions for individuals and companies that benefit from major law firm experience at reasonable rates.

Some areas of emphasis include:

Counseling individuals and companies with respect to clearing, selecting, securing, managing, commercializing, and protecting intellectual property assets around the world. This includes traditional global brand management, marketing, advertising, and enforcement work as well as litigation.
PVT Law Group also provides general counseling services for individuals and businesses, from start-up advice to sophisticated business transactions strategy, agreement negotiating, dispute resolution, and litigation.
Before founding PVT Law Group in 2008, Curtis L. Abernathy led the Trademark, Copyright, & Brand Management Group for Falkner & Ingleby's Seattle office. Curtis was also a senior associate at Silicon Valley based Hartwell, Bexley, Oduya, & Penrose."

Target Market(s)

Clients/potential clients needing tier one, international intellectual property advice with "mega" law firm experience for much less than what we were/would be charging at the "mega firms".

Industry/Entity Type

Legal

Number of Pages Required

4 page

Font styles to use
Serif
Sans Serif

Colors

Designer to choose colors to be used in the design.

Requirements
Must have
• +Improvement over everything on current site at www.pvtlegalhouse.com.
• +Pictures/bios for me and my team (four of us right now).
• +Easy to update and add/remove content.
• +Must be superior in design (look, feel, ease of use, classy and elegant, but hip, reflects international practice).
• +i have logos and color schemes (see current website) but will consider improvements.
Nice to have
• Let me know your thoughts.
Should not have
• No cheese; no overt sales pitches or marketing (since law firm).

```html
<!DOCTYPE html>
<html lang="en">
<head>
<meta charset="utf-8">
<title>PVT Law Group PLLC</title>
<link href="https://fonts.googleapis.com/css2?family=Questrial&family=Lato:ital,wght@0,400;0,700;1,400;1,700;1,900&display=swap" rel="stylesheet">
<style>
:root{
  --orange:#f15a24;
  --orange-soft:#f47a4a;
  --ink:#222222;
  --text:#333333;
  --muted:#8a8a8a;
  --rule:#c9c9c9;
  --panel:#ececec;
  --white:#ffffff;
  --black:#000000;
  --footer-text:#d8d8d8;
}
*{margin:0;padding:0;box-sizing:border-box}
html,body{width:1200px;height:2466px;overflow:hidden;background:var(--white)}
body{position:relative;font-family:'Lato',sans-serif;color:var(--text)}
.abs{position:absolute}
.heading-font{font-family:'Questrial',sans-serif}

/* top bar */
.topbar{left:0;top:0;width:1200px;height:46px;background:var(--orange);color:var(--white);font-size:16px}
.topbar .contact{top:8px;display:flex;align-items:center;gap:10px}
.ring{width:30px;height:30px;border:2px solid var(--white);border-radius:50%;display:flex;align-items:center;justify-content:center}
.topbar .social{right:82px;top:8px;display:flex;gap:6px}

/* header */
.logo{left:82px;top:70px;font-family:'Questrial',sans-serif;font-size:30px;letter-spacing:1px;color:var(--ink)}
.nav{top:88px;font-size:15px;letter-spacing:.5px;color:var(--ink)}
.nav.active{color:var(--orange)}
.nav.active::after{content:"";position:absolute;left:0;right:0;top:28px;height:2px;background:var(--orange)}

/* hero */
.hero{left:0;top:132px;width:1200px;height:550px;background:linear-gradient(180deg,#3a3530 0%,#c98a46 20%,#e8a357 30%,#8a6a52 45%,#4b4a4c 70%,#2b2b2e 100%)}
.hero-band{left:0;top:630px;width:1200px;height:52px;background:rgba(20,20,20,.75);color:var(--white);text-align:center;font-weight:900;font-style:italic;font-size:29px;letter-spacing:1.5px;line-height:52px}
.hero-arrow{top:358px;width:38px;height:36px;background:rgba(30,30,30,.85);display:flex;align-items:center;justify-content:center}

/* welcome */
.section-title{left:0;width:1200px;text-align:center;font-family:'Questrial',sans-serif;font-size:33px;color:var(--ink);letter-spacing:.5px}
.section-title .accent{color:var(--orange)}
.section-title .small{font-size:20px}
.divider{height:2px;background:var(--rule)}
.welcome-copy{left:120px;top:818px;width:960px;text-align:center;font-size:16px;line-height:25px;color:var(--text)}
.welcome-copy strong{color:var(--ink)}
.btn{left:529px;top:995px;width:158px;height:40px;border-radius:20px;background:var(--orange);color:var(--white);font-size:13px;display:flex;align-items:center;padding-left:27px}
.btn .circle{position:absolute;right:6px;top:6px;width:28px;height:28px;border-radius:50%;background:var(--white);display:flex;align-items:center;justify-content:center}

/* practice areas */
.practice{left:0;top:1085px;width:1200px;height:613px;background:var(--panel)}
.card-photo{top:1225px;height:195px;background:var(--white);padding:7px;box-shadow:0 14px 14px -10px rgba(0,0,0,.35)}
.card-photo div{width:100%;height:100%}
.card-title{top:1446px;text-align:center;font-family:'Questrial',sans-serif;font-size:24px;line-height:27px;color:var(--orange-soft)}
.card-copy{top:1513px;text-align:center;font-size:16px;line-height:20px;color:var(--ink)}
.plus{top:1615px;width:33px;height:33px;border-radius:50%;background:var(--orange);display:flex;align-items:center;justify-content:center}

/* commitment & testimonials */
.block-title{top:1744px;font-family:'Questrial',sans-serif;font-size:25px;color:var(--ink);display:flex;align-items:center;gap:12px}
.commit-copy{left:82px;top:1815px;width:500px;font-size:16px;line-height:25px;color:var(--ink)}
.ticks{left:82px;top:1908px;list-style:none;font-size:16px;color:var(--ink)}
.ticks li{display:flex;align-items:center;gap:14px;height:36.5px}
.vsplit{left:600px;top:1745px;width:1px;height:300px;background:linear-gradient(180deg,transparent,#d8d8d8 30%,#d8d8d8 70%,transparent)}
.slide-btn{top:1749px;width:26px;height:26px;border:1px solid #aaa;border-radius:50%;display:flex;align-items:center;justify-content:center;background:var(--white)}
.quote{left:636px;top:1822px;width:482px;font-style:italic;font-size:13px;line-height:21px;color:var(--ink);padding:10px 22px 0 42px}
.avatar{left:659px;top:1958px;width:72px;height:72px;border-radius:50%;background:radial-gradient(circle at 50% 45%,#d9c3b0,#8f7462);border:3px solid var(--white);box-shadow:0 0 0 1px #cfcfcf}
.client-name{left:740px;top:1987px;font-size:13px;font-weight:700;color:var(--ink)}

/* footer */
.footer{left:0;top:2099px;width:1200px;height:318px;background:var(--black);color:var(--footer-text)}
.f-head{top:2143px;font-family:'Questrial',sans-serif;font-size:18px;letter-spacing:1px;color:var(--white)}
.f-rule{top:2170px;height:2px;background:#555}
.f-links{left:82px;top:2197px;list-style:none;font-size:14px;letter-spacing:1px;color:var(--white)}
.f-links li{height:43px;display:flex;align-items:flex-start;gap:10px}
.f-links li::before{content:"›";color:var(--orange);font-size:16px;line-height:16px}
.f-contact{left:265px;top:2200px;font-size:13px;line-height:20px;color:var(--footer-text)}
.f-row{display:flex;gap:12px;align-items:flex-start;margin-bottom:13px}
.f-row b{color:var(--white)}
.map{left:539px;top:2206px;width:266px;height:156px;background:linear-gradient(135deg,#eeeae4,#dedbd5);border:3px solid #f5f5f5}
.f-logo{left:876px;top:2236px;font-family:'Questrial',sans-serif;font-size:24px;letter-spacing:1px;color:#bdbdbd}
.f-social{left:915px;top:2285px;display:flex;gap:8px}
.f-social span{width:34px;height:34px;border-radius:50%;border:2px solid var(--white);background:#1f6fb3}
.copyright{left:0;top:2417px;width:1200px;height:49px;background:var(--orange);color:var(--white);text-align:center;font-size:14px;line-height:49px}
</style>
</head>
<body>

<!-- Top bar -->
<div class="abs topbar">
  <div class="abs contact" style="left:79px">
    <span class="ring"><svg width="14" height="14" viewBox="0 0 24 24"><path fill="#fff" d="M6.6 10.8a15 15 0 0 0 6.6 6.6l2.2-2.2c.3-.3.7-.4 1-.2 1.1.4 2.3.6 3.6.6.6 0 1 .4 1 1V20c0 .6-.4 1-1 1A17 17 0 0 1 3 4c0-.6.4-1 1-1h3.5c.6 0 1 .4 1 1 0 1.3.2 2.5.6 3.6.1.3 0 .7-.2 1z"/></svg></span>
    <span>206.555.0147</span>
  </div>
  <div class="abs contact" style="left:243px">
    <span class="ring"><svg width="14" height="11" viewBox="0 0 24 18"><rect x="1" y="1" width="22" height="16" rx="2" fill="#fff"/><path d="M2 2l10 8 10-8" stroke="#f15a24" stroke-width="2" fill="none"/></svg></span>
    <span>hello@pvtlegalhouse.com</span>
  </div>
  <div class="abs social">
    <span class="ring"></span><span class="ring"></span><span class="ring"></span><span class="ring"></span>
  </div>
</div>

<!-- Header -->
<div class="abs logo">PVT LAW GROUP PLLC</div>
<div class="abs nav active" style="left:630px">HOME</div>
<div class="abs nav" style="left:740px">EXPERIENCE</div>
<div class="abs nav" style="left:891px">ABOUT US</div>
<div class="abs nav" style="left:1026px">CONTACT US</div>

<!-- Hero -->
<div class="abs hero" role="img" aria-label="Aerial photograph of a city skyline at sunset"></div>
<div class="abs hero-band">IMAGINE • SECURE • PROTECT</div>
<div class="abs hero-arrow" style="left:0"><svg width="10" height="14" viewBox="0 0 10 14"><path d="M8 1L2 7l6 6" stroke="#fff" stroke-width="2.5" fill="none"/></svg></div>
<div class="abs hero-arrow" style="right:0"><svg width="10" height="14" viewBox="0 0 10 14"><path d="M2 1l6 6-6 6" stroke="#fff" stroke-width="2.5" fill="none"/></svg></div>

<!-- Welcome -->
<h1 class="abs section-title" style="top:733px;font-weight:400">WELCOME TO <span class="accent">PVT</span> <span class="small">LAW GROUP PLLC</span></h1>
<div class="abs divider" style="left:477px;top:790px;width:246px"></div>
<div class="abs welcome-copy">
  <p>PVT Law Group enjoys providing proactive, business-minded, efficient legal solutions for individuals and companies that benefit from major law firm experience at reasonable rates.</p>
  <p><strong>Some areas of emphasis include:</strong></p>
  <p>• Counseling individuals and companies with respect to clearing, selecting, securing, managing, commercializing, and protecting intellectual property assets around the world. This includes traditional global brand management, marketing, advertising, and enforcement work as well as litigation.</p>
</div>
<div class="abs btn">READ MORE<span class="circle"><svg width="10" height="12" viewBox="0 0 10 12"><path d="M2 1l5 5-5 5" stroke="#f15a24" stroke-width="2.5" fill="none"/></svg></span></div>

<!-- Practice areas -->
<div class="abs practice"></div>
<h2 class="abs section-title" style="top:1130px;font-weight:400">OUR <span class="accent">PRACTICE AREAS</span></h2>
<div class="abs divider" style="left:477px;top:1185px;width:246px"></div>

<div class="abs card-photo" style="left:80px;width:324px"><div role="img" aria-label="Photo of intellectual property word collage" style="background:linear-gradient(135deg,#4f8fa3,#1f4d63)"></div></div>
<div class="abs card-photo" style="left:436px;width:324px"><div role="img" aria-label="Photo of a business presentation in a meeting room" style="background:linear-gradient(135deg,#f2f2f2,#b9c0c8)"></div></div>
<div class="abs card-photo" style="left:792px;width:328px"><div role="img" aria-label="Photo of a handshake over a world map" style="background:linear-gradient(135deg,#1d2a55,#0a1230)"></div></div>

<div class="abs card-title" style="left:80px;width:324px">International Intellectual<br>Property Counseling</div>
<div class="abs card-title" style="left:436px;width:324px">General<br>Corporate</div>
<div class="abs card-title" style="left:792px;width:328px">General<br>Counseling Services</div>

<p class="abs card-copy" style="left:92px;width:300px">Lorem ipsum dolor sit amet, consectetuer adipiscing elit, sed diam nonummy nibh euismod tincidunt ut laoreet dolore magna aliquam erat volutpat.</p>
<p class="abs card-copy" style="left:448px;width:300px">Lorem ipsum dolor sit amet, consectetuer adipiscing elit, sed diam nonummy nibh euismod tincidunt ut laoreet dolore magna aliquam erat volutpat.</p>
<p class="abs card-copy" style="left:806px;width:300px">Lorem ipsum dolor sit amet, consectetuer adipiscing elit, sed diam nonummy nibh euismod tincidunt ut laoreet dolore magna aliquam erat volutpat.</p>

<div class="abs plus" style="left:226px"><svg width="15" height="15" viewBox="0 0 15 15"><path d="M7.5 2v11M2 7.5h11" stroke="#fff" stroke-width="3"/></svg></div>
<div class="abs plus" style="left:582px"><svg width="15" height="15" viewBox="0 0 15 15"><path d="M7.5 2v11M2 7.5h11" stroke="#fff" stroke-width="3"/></svg></div>
<div class="abs plus" style="left:940px"><svg width="15" height="15" viewBox="0 0 15 15"><path d="M7.5 2v11M2 7.5h11" stroke="#fff" stroke-width="3"/></svg></div>

<!-- Commitment -->
<h3 class="abs block-title" style="left:82px;font-weight:400">
  <svg width="30" height="20" viewBox="0 0 30 20"><path d="M2 8l7-6 6 4 6-4 7 6-10 10z" fill="none" stroke="#f15a24" stroke-width="2.5" stroke-linejoin="round"/></svg>
  OUR COMMITMENT TO CUSTOMER
</h3>
<div class="abs divider" style="left:82px;top:1791px;width:430px;height:1px"></div>
<p class="abs commit-copy">Loren&nbsp; autem vel eum iriure hendrerit in vulputate velit esse molestie. onsectetuer adipiscing elit, sed diam nonummy nibh euismod tincidunt u eu feugiat nulla facilisis.</p>
<ul class="abs ticks">
  <li><svg width="16" height="16" viewBox="0 0 16 16"><circle cx="8" cy="8" r="8" fill="#f15a24"/><path d="M4 8l3 3 5-6" stroke="#fff" stroke-width="2" fill="none"/></svg>Autem vel eum iriure hendrerit in</li>
  <li><svg width="16" height="16" viewBox="0 0 16 16"><circle cx="8" cy="8" r="8" fill="#f15a24"/><path d="M4 8l3 3 5-6" stroke="#fff" stroke-width="2" fill="none"/></svg>Gendrerit in vulputate velit</li>
  <li><svg width="16" height="16" viewBox="0 0 16 16"><circle cx="8" cy="8" r="8" fill="#f15a24"/><path d="M4 8l3 3 5-6" stroke="#fff" stroke-width="2" fill="none"/></svg>Autem vel eum adipiscing elit, sed diam</li>
  <li><svg width="16" height="16" viewBox="0 0 16 16"><circle cx="8" cy="8" r="8" fill="#f15a24"/><path d="M4 8l3 3 5-6" stroke="#fff" stroke-width="2" fill="none"/></svg>Eeum iriure hendrerit in vulputate velit</li>
</ul>
<div class="abs vsplit"></div>

<!-- Testimonials -->
<h3 class="abs block-title" style="left:633px;font-weight:400">
  <svg width="24" height="22" viewBox="0 0 24 22"><path d="M1 1h15v10H7l-4 4v-4H1z" fill="#f15a24"/><path d="M18 6h5v10h-2v4l-4-4h-7v-3h8z" fill="#f15a24"/></svg>
  CLIENT TESTIMONIALS
</h3>
<div class="abs divider" style="left:633px;top:1791px;width:290px;height:1px"></div>
<div class="abs slide-btn" style="left:1061px"><svg width="8" height="10" viewBox="0 0 8 10"><path d="M6 1L2 5l4 4" stroke="#777" stroke-width="1.5" fill="none"/></svg></div>
<div class="abs slide-btn" style="left:1094px"><svg width="8" height="10" viewBox="0 0 8 10"><path d="M2 1l4 4-4 4" stroke="#777" stroke-width="1.5" fill="none"/></svg></div>
<svg class="abs" style="left:636px;top:1820px" width="484" height="160" viewBox="0 0 484 160">
  <path d="M8 2h468a6 6 0 0 1 6 6v126a6 6 0 0 1-6 6H398l-20 18-8-18H8a6 6 0 0 1-6-6V8a6 6 0 0 1 6-6z" fill="#fff" stroke="#cfcfcf" stroke-width="1.5"/>
  <path d="M24 18h8l-4 10h4v8h-10v-8zM38 18h8l-4 10h4v8h-10v-8z" fill="#bdbdbd"/>
</svg>
<p class="abs quote">Lorem ipsum dolor sit amet consetug e sed diay nibh euismodl tincidunt ut laoreet dolore magam er vol wisi enim ad minim veniam quis nostrud exerci tationorem ipsum dolor sit ametee sed diammmy nibh euismd tincidunt ut laoreet dolore magna aliqur volpatl tiidunt ut laoreet dolore magna aliqur volpatl r sit ametee.</p>
<div class="abs avatar" role="img" aria-label="Client portrait photo"></div>
<div class="abs client-name">Mrs. Laura Pennick</div>

<!-- Footer -->
<div class="abs footer"></div>
<div class="abs f-head" style="left:82px">QUICK LINKS</div>
<div class="abs f-rule" style="left:82px;width:92px"></div>
<ul class="abs f-links">
  <li>HOME</li><li>EXPERIENCE</li><li>ABOUT US</li><li>CONTACT US</li>
</ul>

<div class="abs f-head" style="left:265px">CONTACT DETAILS</div>
<div class="abs f-rule" style="left:265px;width:92px"></div>
<div class="abs f-contact">
  <div class="f-row"><svg width="14" height="18" viewBox="0 0 14 18"><path d="M7 0a7 7 0 0 1 7 7c0 5-7 11-7 11S0 12 0 7a7 7 0 0 1 7-7z" fill="#f15a24"/><circle cx="7" cy="7" r="2.5" fill="#000"/></svg><div><b>PVT LAW GROUP PLLC</b><br>450 Linden Ave. Suite B.<br>SEATTLE WA. 98109</div></div>
  <div class="f-row"><svg width="14" height="14" viewBox="0 0 24 24"><path fill="#f15a24" d="M6.6 10.8a15 15 0 0 0 6.6 6.6l2.2-2.2c.3-.3.7-.4 1-.2 1.1.4 2.3.6 3.6.6.6 0 1 .4 1 1V20c0 .6-.4 1-1 1A17 17 0 0 1 3 4c0-.6.4-1 1-1h3.5c.6 0 1 .4 1 1 0 1.3.2 2.5.6 3.6.1.3 0 .7-.2 1z"/></svg><b>206.555.0147</b></div>
  <div class="f-row"><svg width="14" height="14" viewBox="0 0 14 14"><rect x="3" y="0" width="8" height="5" fill="#f15a24"/><rect x="0" y="5" width="14" height="6" rx="1" fill="#f15a24"/><rect x="3" y="9" width="8" height="5" fill="#f15a24"/></svg><b>206.555.0148</b></div>
  <div class="f-row"><svg width="14" height="11" viewBox="0 0 24 18"><rect x="1" y="1" width="22" height="16" rx="2" fill="#f15a24"/><path d="M2 2l10 8 10-8" stroke="#000" stroke-width="2" fill="none"/></svg>hello@pvtlegalhouse.com</div>
</div>

<div class="abs f-head" style="left:538px">LOCATION MAP</div>
<div class="abs f-rule" style="left:538px;width:112px"></div>
<div class="abs map" role="img" aria-label="Street map showing the office location"></div>

<div class="abs f-logo">PVT LAW GROUP PLLC</div>
<div class="abs f-social"><span></span><span></span><span></span><span style="background:#d2452b"></span></div>

<div class="abs copyright">Copyright © 2017&nbsp; PVT LAW GROUP PLLC. All Rights Reserved.</div>

</body>
</html>
```